Financial Advisor Website Design

We are working with KLV•ARO. They are a financial advising company that needs a new website design.

Some sites to use for inspiration:

https://investor.quillmarsh.com
https://www.hollisbrant.com/us-en
https://www.corvantel.com
https://www.aboutpellgrew.com

Thank you for taking the time to consider designing a website for us. We are web developers based in Stockton and Los Angeles, CA, USA. Most of our projects go through the same process. Understanding this process may help you win a project with us. We custom-code all of our websites in-house. We don’t have any requirements as to what tools you use for your design, but we prefer Figma files. For any design that we label as four-stars, we send it to the client for review. The client picks the final design they want us to use. Once we complete this process, we will continue to show additional clients all the four-star sites and purchase them later. Your designs will have multiple chances to sell. For better chances of success, we ask that you follow these guidelines.

IMAGES:
If you use any images or icons in the design, we ask that you have a link to the asset so we can purchase the image/icon. Most of the designs we submit do not have the customer’s images on them unless they have some great images. Be creative; show us the feeling you are trying to portray with your image choices. Use any royalty-free site you choose. We subscribe to Parvel and mainly use their images, but we can purchase images outside of Parvel.

PLEASE NOTE: we will not submit designs to clients with watermarks on the images.

FONTS:
We ask that you identify the fonts used in the design. This can be done in a message if you want. We typically use Tessly Fonts and Parvel Fonts.

CONTENT:
We're always open to different content and ideas. We often submit designs with stock images so the client can see our vision. We typically take pictures after the website launch to use their images with our vision. Lorem Ipsum is fine for paragraphs, but we ask that you write the headers in correct English. We want to be able to show the vision and identify the sections of the website.

INSPIRATION:
We typically add a couple of links in the brief of websites we like to help you get started in your design.

REVISIONS:
We do not often ask for revisions of the designs unless we see something in the design that may not appeal to the client. If there are slight changes that we want to make, we do that in the development process.

FEEDBACK:
We rarely give feedback on designs during the design process. We are working on many website projects and do not have the time to provide feedback. We usually respond if your request is well thought out and asks specific questions, but a note asking “feedback, please” usually goes unanswered.

```html
<!DOCTYPE html>
<html lang="en">
<head>
<meta charset="utf-8">
<title>KLV•ARO — Financial Advising</title>
<link rel="stylesheet" href="https://fonts.googleapis.com/css2?family=Montserrat:wght@400;500;600;700;800&display=swap">
<style>
:root{
  --navy:#16336b;
  --navy-deep:#0d2350;
  --gold:#d6b526;
  --ink:#2b2b2b;
  --muted:#5a5a5a;
  --light:#f2f2f2;
  --footer:#1f1f1f;
  --white:#ffffff;
}
*{box-sizing:border-box;margin:0;padding:0}
html,body{width:1200px;height:4367px;overflow:hidden}
body{font-family:"Montserrat",sans-serif;color:var(--ink);background:var(--white);position:relative}
.abs{position:absolute}
a{color:inherit;text-decoration:none}

/* hero */
.hero{position:absolute;left:0;top:0;width:1200px;height:760px;
  background:linear-gradient(180deg,#1d1f22 0%,#3a3630 35%,#4a4238 60%,#2a2826 100%)}
.hero-photo{position:absolute;inset:0;background:
  radial-gradient(ellipse at 75% 35%,rgba(170,150,120,.45),transparent 55%),
  radial-gradient(ellipse at 20% 60%,rgba(60,80,50,.5),transparent 50%),
  linear-gradient(180deg,rgba(0,0,0,.55),rgba(0,0,0,.25) 40%,rgba(0,0,0,.5))}
.hero-cut{position:absolute;left:0;bottom:0}
.nav a{position:absolute;top:56px;font-size:14px;font-weight:500;color:var(--white)}
.nav a.active{color:var(--gold);text-decoration:underline;text-underline-offset:4px}
.nav-name{position:absolute;left:500px;top:64px;width:200px;text-align:center;color:var(--white);
  font-weight:600;font-size:22px;letter-spacing:3px}
.btn-login{position:absolute;left:997px;top:46px;width:129px;height:41px;background:var(--gold);
  color:var(--white);font-weight:700;font-size:14px;display:flex;align-items:center;justify-content:center}
.hero-title{position:absolute;left:0;width:1200px;top:300px;text-align:center;color:var(--white);
  font-weight:800;font-size:100px;line-height:1;letter-spacing:2px}
.hero-tag{position:absolute;left:0;width:1200px;top:420px;text-align:center;color:var(--white);
  font-weight:500;font-size:28px;line-height:36px}
.btn{position:absolute;background:var(--gold);color:var(--white);font-weight:600;font-size:15px;
  display:flex;align-items:center;justify-content:center;letter-spacing:.5px}

/* about */
.about-frame{left:75px;top:822px;width:422px;height:493px;background:var(--gold)}
.about-photo{left:136px;top:885px;width:450px;height:369px;
  background:linear-gradient(135deg,#6d5a48 0%,#a88e72 40%,#d9cbb6 70%,#8a7765 100%)}
.about-title{left:614px;top:884px;font-size:38px;font-weight:500;color:var(--navy);letter-spacing:1px}
.about-text{left:614px;width:510px;font-size:13.5px;line-height:24px;color:var(--muted)}

/* services */
.services-bg{left:0;top:1455px;width:1200px;height:548px;
  background:linear-gradient(180deg,#ffffff 0%,#e9eef3 30%,#d8dee6 55%,#eef1f4 80%,#dde3ea 100%)}
.section-title{position:absolute;left:0;width:1200px;text-align:center;font-size:38px;font-weight:500;color:var(--ink);letter-spacing:1px}
.svc{position:absolute;width:328px;height:212px;background:var(--white);padding:28px 18px 0 18px;overflow:hidden}
.svc::after{content:"";position:absolute;right:0;bottom:0;border-style:solid;border-width:0 0 44px 44px;
  border-color:transparent transparent var(--gold) transparent}
.svc.featured{background:linear-gradient(135deg,var(--gold) 0%,#5a6a45 45%,var(--navy) 100%)}
.svc.featured::after{display:none}
.svc h3{margin-top:14px;font-size:16px;font-weight:600;line-height:24px;color:var(--navy);letter-spacing:.5px}
.svc p{margin-top:8px;font-size:13px;line-height:20px;color:var(--muted);width:280px}
.svc.featured h3,.svc.featured p{color:var(--white)}
.svc svg{display:block}

/* why */
.why{left:0;top:2003px;width:1200px;height:500px;
  background:linear-gradient(135deg,#1b3a78 0%,var(--navy) 50%,#0f2a5c 100%)}
.why .section-title{color:var(--white);top:70px}
.why-card{position:absolute;top:139px;width:242px;height:288px;background:var(--white);text-align:center}
.why-card .v{position:absolute;left:0;top:0}
.why-card .dot{position:absolute;left:75px;top:46px;width:92px;height:92px;border-radius:50%;background:var(--navy);
  display:flex;align-items:center;justify-content:center}
.why-card h4{position:absolute;left:0;width:100%;top:158px;font-size:17px;font-weight:600;line-height:24px;color:var(--navy)}
.why-card p{position:absolute;left:20px;width:202px;top:212px;font-size:13.5px;line-height:20px;color:var(--muted)}

/* stories */
.stories-title{left:75px;top:2556px;font-size:38px;font-weight:500;letter-spacing:1px}
.story-photo{width:180px;height:181px;top:2636px}
.quote-mark{font-size:70px;font-weight:800;color:var(--gold);line-height:1;top:2628px;font-family:Georgia,serif}
.quote{top:2690px;width:290px;font-size:17px;line-height:25px;color:var(--ink)}
.quote-name{top:2793px;font-size:17px;font-weight:700;color:var(--navy)}

/* insights */
.insights{left:0;top:2895px;width:1200px;height:500px;background:var(--light)}
.insight-main{left:75px;top:3036px;width:512px;height:292px;
  background:linear-gradient(135deg,#c9ced6 0%,#8b96a6 40%,#4a4a50 75%,#2c2c30 100%)}
.insight-band{left:75px;top:3243px;width:512px;height:85px;background:rgba(0,0,0,.55);
  padding:16px 20px;color:var(--white);font-size:24px;line-height:30px}
.insight-thumb{left:615px;width:221px;height:136px}
.insight-text{left:854px;width:290px;font-size:24px;line-height:31px;color:var(--navy)}

/* cta */
.cta{left:0;top:3395px;width:1200px;height:382px;
  background:radial-gradient(ellipse at 30% 100%,rgba(40,80,180,.6),transparent 55%),
  linear-gradient(180deg,#0f2d72 0%,#13388a 50%,#0b2150 100%)}
.cta h2{position:absolute;left:0;width:1200px;top:82px;text-align:center;color:var(--white);font-size:38px;font-weight:500;line-height:40px;letter-spacing:1px}
.cta p{position:absolute;left:230px;width:740px;top:168px;text-align:center;color:var(--white);font-size:16px;line-height:26px;font-weight:500}

/* contact strip */
.contact-name{left:98px;top:3870px;width:200px;text-align:center;color:var(--navy);font-weight:600;font-size:26px;letter-spacing:3px}
.contact-col h5{font-size:17px;font-weight:600;color:var(--navy);letter-spacing:.5px;margin-top:16px}
.contact-col p{font-size:15px;line-height:25px;color:var(--ink);margin-top:4px}

/* footer */
.footer{left:0;top:3982px;width:1200px;height:385px;background:var(--footer)}
.foot-col h6{font-size:17px;font-weight:600;color:var(--gold);letter-spacing:.5px;margin-bottom:12px}
.foot-col li{list-style:none;font-size:14px;line-height:32px;color:#d8d8d8}
.foot-col p{font-size:14px;line-height:25px;color:#d8d8d8}
.email{left:885px;top:4136px;width:241px;height:47px;border:1px solid #777;color:var(--white);font-size:12px;padding:0 16px;display:flex;align-items:center;font-weight:500}
.subscribe{left:885px;top:4197px;width:241px;height:46px;background:var(--navy);color:var(--white);font-size:14px;font-weight:600;display:flex;align-items:center;justify-content:center;letter-spacing:.5px}
.foot-rule{left:0;top:4302px;width:1200px;height:1px;background:#3a3a3a}
.copyright{left:73px;top:4327px;font-size:11px;color:#cfcfcf}
.social{top:4326px;font-size:11px;font-weight:600;color:#cfcfcf}
</style>
</head>
<body>

<!-- HERO -->
<header class="hero">
  <div class="hero-photo" role="img" aria-label="Advisors meeting in a bright modern office, dark toned"></div>
  <nav class="nav">
    <a class="active" style="left:97px">Home</a>
    <a style="left:185px">About Us</a>
    <a style="left:297px">Services</a>
    <a style="left:400px">Partners</a>
    <a style="left:743px">Careers</a>
    <a style="left:842px">Blog</a>
    <a style="left:918px">Contact</a>
  </nav>
  <div class="nav-name">KLV•ARO</div>
  <a class="btn-login">Secure Login</a>
  <h1 class="hero-title">KLV•ARO</h1>
  <p class="hero-tag">We are a financial advising company.</p>
  <a class="btn" style="left:520px;top:493px;width:160px;height:48px">LEARN MORE</a>
  <svg class="abs" style="left:590px;top:594px" width="20" height="36" viewBox="0 0 20 36"><path d="M10 0v32M3 25l7 8 7-8" stroke="#fff" stroke-width="3" fill="none"/></svg>
  <svg class="hero-cut" width="1200" height="120" viewBox="0 0 1200 120"><polygon points="0,120 0,110 229,56 340,73 598,10 950,64 1200,100 1200,120" fill="#fff"/></svg>
</header>

<!-- ABOUT -->
<section>
  <div class="abs about-frame"></div>
  <div class="abs about-photo" role="img" aria-label="Older couple reviewing a document with their female advisor"></div>
  <h2 class="abs about-title">ABOUT KLV•ARO</h2>
  <p class="abs about-text" style="top:942px">Nemo enim ipsam voluptatem quia voluptas sit aspernatur aut odit aut fugit, sed quia consequuntur magni dolores eos qui ratione voluptatem sequi nesciunt. Neque porro quisquam est, qui dolorem ipsum quia dolor sit amet, consectetur, adipisci velit, sed quia non numquam eius modi tempora incidunt ut labore et dolore magnam aliquam quaerat voluptatem.</p>
  <p class="abs about-text" style="top:1101px">Nemo enim ipsam voluptatem quia voluptas sit aspernatur aut odit aut fugit, sed quia consequuntur magni dolores eos qui ratione voluptatem sequi nesciunt. .</p>
  <a class="btn" style="left:614px;top:1198px;width:159px;height:48px">LEARN MORE</a>
</section>

<!-- SERVICES -->
<section>
  <div class="abs services-bg" role="img" aria-label="Snowy mountain range backdrop"></div>
  <h2 class="section-title" style="top:1390px">OUR SERVICES</h2>

  <div class="svc" style="left:75px;top:1473px">
    <svg width="32" height="28" viewBox="0 0 32 28"><g fill="#16336b"><rect y="3" width="32" height="4"/><rect y="12" width="32" height="4"/><rect y="21" width="32" height="4"/></g><g fill="#d6b526"><rect x="6" y="1" width="5" height="8"/><rect x="19" y="10" width="5" height="8"/><rect x="10" y="19" width="5" height="8"/></g></svg>
    <h3>FINANCIAL PLANNING<br>&amp; STRATEGY</h3>
    <p>Nemo enim ipsam voluptatem quia voluptas sit aspernatur aut odit aut fugit, sed quia .</p>
  </div>
  <div class="svc featured" style="left:436px;top:1473px">
    <svg width="24" height="30" viewBox="0 0 24 30"><path d="M2 2h13l7 7v19H2z" fill="none" stroke="#fff" stroke-width="3"/><path d="M7 15h10M7 21h10" stroke="#fff" stroke-width="2.5"/></svg>
    <h3>RETIREMENT<br>PLANNING</h3>
    <p>Nemo enim ipsam voluptatem quia voluptas sit aspernatur aut odit aut fugit, sed quia .</p>
  </div>
  <div class="svc" style="left:797px;top:1473px">
    <svg width="34" height="26" viewBox="0 0 34 26"><g fill="#16336b"><circle cx="17" cy="7" r="6"/><circle cx="6" cy="10" r="4"/><circle cx="28" cy="10" r="4"/><path d="M7 26c0-8 4-11 10-11s10 3 10 11z"/><path d="M0 24c0-6 3-8 6-8s4 1 4 1l-2 7z"/><path d="M34 24c0-6-3-8-6-8s-4 1-4 1l2 7z"/></g></svg>
    <h3>INVESTMENT<br>ADVISORY</h3>
    <p>Nemo enim ipsam voluptatem quia voluptas sit aspernatur aut odit aut fugit, sed quia .</p>
  </div>

  <div class="svc" style="left:75px;top:1715px">
    <svg width="26" height="30" viewBox="0 0 26 30"><rect x="1" y="1" width="24" height="28" rx="3" fill="#16336b"/><rect x="5" y="5" width="16" height="6" fill="#fff"/><g fill="#fff"><rect x="5" y="14" width="4" height="4"/><rect x="11" y="14" width="4" height="4"/><rect x="17" y="14" width="4" height="4"/><rect x="5" y="21" width="4" height="4"/><rect x="11" y="21" width="4" height="4"/><rect x="17" y="21" width="4" height="4"/></g></svg>
    <h3>TAX<br>OPTIMIZATION</h3>
    <p>Nemo enim ipsam voluptatem quia voluptas sit aspernatur aut odit aut fugit, sed quia .</p>
  </div>
  <div class="svc" style="left:436px;top:1715px">
    <svg width="30" height="30" viewBox="0 0 30 30"><path d="M1 14C2 6 8 2 15 2s13 4 14 12z" fill="#16336b"/><path d="M15 14v10a3 3 0 0 1-6 0" stroke="#d6b526" stroke-width="3" fill="none"/></svg>
    <h3>INSURANCE &amp; RISK<br>MANAGEMENT</h3>
    <p>Nemo enim ipsam voluptatem quia voluptas sit aspernatur aut odit aut fugit, sed quia .</p>
  </div>
  <div class="svc" style="left:797px;top:1715px">
    <svg width="28" height="28" viewBox="0 0 28 28"><rect x="1" y="7" width="26" height="20" rx="3" fill="#16336b"/><path d="M9 7V3h10v4" stroke="#16336b" stroke-width="3" fill="none"/></svg>
    <h3>BUSINESS FINANCIAL<br>CONSULTING</h3>
    <p>Nemo enim ipsam voluptatem quia voluptas sit aspernatur aut odit aut fugit, sed quia .</p>
  </div>
</section>

<!-- WHY CHOOSE -->
<section class="abs why">
  <h2 class="section-title">WHY CHOOSE KLV-ARO</h2>

  <div class="why-card" style="left:75px">
    <svg class="v" width="242" height="70" viewBox="0 0 242 70"><polygon points="0,0 242,0 242,14 121,70 0,14" fill="#d6b526"/></svg>
    <div class="dot"><svg width="24" height="30" viewBox="0 0 24 30"><circle cx="12" cy="11" r="10" fill="#fff"/><rect x="7" y="20" width="10" height="6" fill="#fff"/></svg></div>
    <h4>TAILORED<br>SOLUTIONS</h4>
    <p>Every plan is custom-built for your goals</p>
  </div>
  <div class="why-card" style="left:346px">
    <svg class="v" width="242" height="70" viewBox="0 0 242 70"><polygon points="0,0 242,0 242,14 121,70 0,14" fill="#d6b526"/></svg>
    <div class="dot"><svg width="30" height="28" viewBox="0 0 30 28"><rect x="1" y="12" width="6" height="15" fill="#fff"/><path d="M10 12l6-11c3 0 4 2 3 5l-1 5h9c2 0 3 2 2 4l-3 10c-1 2-2 2-4 2H10z" fill="#fff"/></svg></div>
    <h4>PROVEN<br>EXPERTISE</h4>
    <p>Decades of combined experience in wealth management.</p>
  </div>
  <div class="why-card" style="left:615px">
    <svg class="v" width="242" height="70" viewBox="0 0 242 70"><polygon points="0,0 242,0 242,14 121,70 0,14" fill="#d6b526"/></svg>
    <div class="dot"><svg width="28" height="28" viewBox="0 0 28 28"><circle cx="14" cy="8" r="7" fill="#fff"/><path d="M1 28c0-8 6-12 13-12s13 4 13 12z" fill="#fff"/></svg></div>
    <h4>CLIENT-FIRST<br>APPROACH</h4>
    <p>Transparent, unbiased financial advice.</p>
  </div>
  <div class="why-card" style="left:883px">
    <svg class="v" width="242" height="70" viewBox="0 0 242 70"><polygon points="0,0 242,0 242,14 121,70 0,14" fill="#d6b526"/></svg>
    <div class="dot"><svg width="34" height="28" viewBox="0 0 34 28"><ellipse cx="13" cy="11" rx="12" ry="9" fill="#fff"/><path d="M4 17l-3 7 8-4z" fill="#fff"/><ellipse cx="23" cy="16" rx="10" ry="7" fill="#fff" stroke="#16336b" stroke-width="2"/></svg></div>
    <h4>ONGOING<br>SUPPORT</h4>
    <p>Continuous monitoring and adjustments as your life evolves.</p>
  </div>
</section>

<!-- CLIENT SUCCESS STORIES -->
<section>
  <h2 class="abs stories-title">CLIENT SUCCESS STORIES</h2>
  <svg class="abs" style="left:1080px;top:2568px" width="46" height="30" viewBox="0 0 46 30"><path d="M14 3L4 15l10 12" stroke="#2b2b2b" stroke-width="3" fill="none"/><path d="M30 3l10 12-10 12" stroke="#d6b526" stroke-width="3" fill="none"/></svg>

  <div class="abs story-photo" style="left:75px;background:linear-gradient(135deg,#cfd6dc,#8e99a6 50%,#2e3a4a)" role="img" aria-label="Smiling businessman holding a tablet in an office"></div>
  <div class="abs quote-mark" style="left:272px">“</div>
  <p class="abs quote" style="left:275px">" Excepteur sint occaecat cupidatat non proident, sunt in culpa qui officia deserunt mollit anim id est laborum."</p>
  <div class="abs quote-name" style="left:275px">Name Heading</div>

  <div class="abs story-photo" style="left:617px;background:linear-gradient(135deg,#e4e6e8,#a9b3be 50%,#3e5a86)" role="img" aria-label="Smiling man in a blue suit holding a clipboard"></div>
  <div class="abs quote-mark" style="left:819px">“</div>
  <p class="abs quote" style="left:822px">" Excepteur sint occaecat cupidatat non proident, sunt in culpa qui officia deserunt mollit anim id est laborum."</p>
  <div class="abs quote-name" style="left:822px">Name Heading</div>
</section>

<!-- LATEST INSIGHTS -->
<section class="abs insights"></section>
<h2 class="section-title" style="top:2952px">LATEST INSIGHTS</h2>
<div class="abs insight-main" role="img" aria-label="Woman analysing financial charts on a monitor"></div>
<div class="abs insight-band">Nemo enim ipsam voluptatem quia voluptas sit aspernatur.</div>
<div class="abs insight-thumb" style="top:3036px;background:linear-gradient(135deg,#8b8a86,#c2b8a8 50%,#4d4f55)" role="img" aria-label="Advisor meeting with a senior couple at a table"></div>
<p class="abs insight-text" style="top:3055px">Nemo enim ipsam voluptatem quia volu ptas sit aspernatur.</p>
<div class="abs insight-thumb" style="top:3193px;background:linear-gradient(135deg,#1b2b36,#3d5a4a 50%,#7a6a3a)" role="img" aria-label="Hands holding a small plant growing from coins"></div>
<p class="abs insight-text" style="top:3212px">Nemo enim ipsam voluptatem quia volu ptas sit aspernatur.</p>

<!-- CTA -->
<section class="abs cta" role="img" aria-label="Stacked coins in deep blue light">
  <h2>READY TO BUILD<br>YOUR FINANCIAL FREEDOM?</h2>
  <p>Nemo enim ipsam voluptatem quia voluptas sit aspernatur aut odit aut fugit, sed quia consequuntur magni dolores eos qui ratione.</p>
</section>
<a class="btn" style="left:425px;top:3641px;width:348px;height:51px;color:var(--navy);font-weight:700">Schedule Your Free Consultation</a>

<!-- CONTACT STRIP -->
<section>
  <div class="abs contact-name">KLV•ARO</div>
  <div class="abs contact-col" style="left:352px;top:3832px">
    <svg width="26" height="20" viewBox="0 0 26 20"><path d="M1 3l7-2 10 3 7-2v15l-7 2-10-3-7 2z" fill="#d6b526"/></svg>
    <h5>ADDRESS</h5>
    <p style="font-size:13.5px;line-height:24px">48 Harrow Lane Suite 12,<br>Brookdale 20417, United State</p>
  </div>
  <div class="abs contact-col" style="left:663px;top:3832px">
    <svg width="22" height="22" viewBox="0 0 22 22"><path d="M4 1l4 5-2 3c1 3 4 6 7 7l3-2 5 4-3 4C9 22 0 13 0 4z" fill="#d6b526"/></svg>
    <h5>PHONE</h5>
    <p>+144-555-0190</p>
  </div>
  <div class="abs contact-col" style="left:885px;top:3832px">
    <svg width="24" height="20" viewBox="0 0 24 20"><rect y="2" width="24" height="16" rx="2" fill="#d6b526"/><path d="M1 4l11 8 11-8" stroke="#fff" stroke-width="2" fill="none"/></svg>
    <h5>ENVELOPE</h5>
    <p>hello@klvaro-mail.com</p>
  </div>
</section>

<!-- FOOTER -->
<footer class="abs footer"></footer>
<div class="abs foot-col" style="left:73px;top:4036px">
  <h6>QUICK LINKS</h6>
  <ul><li>Home</li><li>About Us</li><li>Services</li><li>Partners</li></ul>
</div>
<div class="abs foot-col" style="left:215px;top:4068px">
  <ul><li>Careers</li><li>Blog</li><li>Contact</li></ul>
</div>
<div class="abs foot-col" style="left:344px;top:4036px">
  <h6>SERVICES</h6>
  <ul><li>Financial Planning &amp; Strategy</li><li>Retirement Planning</li><li>Investment Advisory</li><li>Tax Optimization</li><li>Insurance &amp; Risk Management</li><li>Business Financial Consulting</li></ul>
</div>
<div class="abs foot-col" style="left:656px;top:4036px">
  <h6>LEGAL</h6>
  <ul><li>Duis aute irure</li><li>Dolor in reprehenderit</li><li>Voluptate velit</li><li>Esse cillum dolore</li><li>Eufugiat</li></ul>
</div>
<div class="abs foot-col" style="left:885px;top:4036px;width:240px">
  <h6>NEWSLETTER</h6>
  <p>Duis aute irure dolor in repre henderit in voluptate.</p>
</div>
<div class="abs email">Email Address</div>
<div class="abs subscribe">SUBSCRIBE</div>
<div class="abs foot-rule"></div>
<p class="abs copyright">Copyright © 2025 Company Name All Rights Reserved.</p>
<span class="abs social" style="left:930px">Frondly</span>
<span class="abs social" style="left:985px">Zestr</span>
<span class="abs social" style="left:1028px">Pictora</span>
<span class="abs social" style="left:1078px">Linkvale</span>
<span class="abs social" style="left:1136px">Vidora</span>

</body>
</html>
```